Pennfield Hearing Clinic Business Card Design Project

We need a new business card design. We changed our logo recently and need to update our cards. We are a small hearing clinic with a 3 locations in BC. We help people with hearing loss by fitting them with hearing instruments that are appropriate for them and help them overcome the challenges that hearing loss causes. The symbol part of our logo represents the three important components of successful outcome. The three are: 1-acceptance of the change in hearing, 2-a hearing care provider that cares and is knowledgeable and experienced, 3-a quality hearing instrument. I would like to have a clean design that shows quality commitment to a successful end result of treatment. Here is our website for more information. www.sonvale.ca

Target Market(s)

Senior population - mostly 50+

Industry/Entity Type

Clinic

Requirements
Must have
• Logo
Name - Derek Olsbrand
Title - Hearing Instrument Practitioner (can be very small)
Phone: 250 637-5814
Address: 415-B 22nd Street, Alder Bay, BC V0N 7K3
Email: derek@sonvale.ca
website address: www.sonvale.ca
Nice to have
• Could be both sided and have a photo on the card.

```html
<!DOCTYPE html>
<html lang="en">
<head>
<meta charset="utf-8">
<title>Pennfield Hearing Clinic – Business Card</title>
<link rel="stylesheet" href="https://fonts.googleapis.com/css2?family=Cabin:wght@400;600;700&display=swap">
<style>
  :root {
    --page: #c9c9c9;
    --card: #fbfbf9;
    --orange: #ee9024;
    --blue: #2a6db5;
    --green: #84c341;
    --band-text: #1f5aa6;
    --photo-warm: #c9782c;
    --photo-cool: #4a4a8a;
  }
  * { box-sizing: border-box; margin: 0; padding: 0; }
  html, body { width: 1200px; height: 747px; overflow: hidden; }
  body {
    background: var(--page);
    font-family: "Cabin", "Gill Sans", sans-serif;
    display: flex;
    flex-direction: column;
    align-items: center;
    justify-content: center;
    gap: 34px;
  }
  .card {
    position: relative;
    width: 600px;
    height: 343px;
    background: var(--card);
    overflow: hidden;
    box-shadow: 0 4px 14px rgba(0,0,0,.18);
  }

  /* Front */
  .brand {
    position: absolute;
    top: 28px;
    right: 34px;
    display: flex;
    align-items: center;
    gap: 10px;
  }
  .brand-dot {
    width: 22px; height: 22px;
    border-radius: 50%;
    background: var(--orange);
  }
  .brand-name {
    color: var(--blue);
    font-weight: 700;
    font-size: 22px;
    letter-spacing: -.3px;
  }
  .person {
    position: absolute;
    top: 34px;
    left: 34px;
  }
  .person-name {
    color: var(--orange);
    font-weight: 700;
    font-size: 28px;
    letter-spacing: 1.5px;
  }
  .person-title {
    color: var(--blue);
    font-size: 13px;
    margin-top: 2px;
    letter-spacing: .3px;
  }
  .portrait {
    position: absolute;
    top: 112px;
    left: 34px;
    width: 190px;
    height: 150px;
    background: linear-gradient(135deg, var(--photo-warm) 0%, #d99046 45%, var(--photo-cool) 100%);
  }
  .address {
    position: absolute;
    right: 34px;
    bottom: 58px;
    color: var(--orange);
    font-size: 15px;
    letter-spacing: .4px;
  }
  .contact-band {
    position: absolute;
    left: 0; right: 0; bottom: 0;
    height: 44px;
    background: var(--green);
    display: flex;
    justify-content: space-between;
    align-items: center;
    padding: 0 34px;
    color: var(--band-text);
    font-size: 15px;
    letter-spacing: .4px;
  }

  /* Back */
  .back-brand {
    position: absolute;
    top: 120px; left: 0; right: 0;
    display: flex;
    justify-content: center;
    align-items: center;
    gap: 14px;
  }
  .back-dot {
    width: 34px; height: 34px;
    border-radius: 50%;
    background: var(--orange);
  }
  .back-name {
    color: var(--blue);
    font-weight: 700;
    font-size: 38px;
    letter-spacing: -.5px;
  }
  .back-web {
    position: absolute;
    left: 0; right: 0; bottom: 58px;
    text-align: center;
    color: var(--blue);
    font-size: 20px;
    letter-spacing: .6px;
  }
</style>
</head>
<body>
  <section class="card front" aria-label="Business card front">
    <div class="brand">
      <span class="brand-dot"></span>
      <span class="brand-name">Pennfield Hearing Clinic</span>
    </div>
    <div class="person">
      <h1 class="person-name">Derek Olsbrand</h1>
      <p class="person-title">Hearing Instrument Practitioner</p>
    </div>
    <div class="portrait" role="img" aria-label="Photo of the practitioner and a colleague in the clinic"></div>
    <p class="address">415-B 22nd Street, Alder Bay, BC V0N 7K3</p>
    <div class="contact-band">
      <span class="web">www.sonvale.ca</span>
      <span class="email">derek@sonvale.ca</span>
      <span class="phone">250 637-5814</span>
    </div>
  </section>

  <section class="card back" aria-label="Business card back">
    <div class="back-brand">
      <span class="back-dot"></span>
      <span class="back-name">Pennfield Hearing Clinic</span>
    </div>
    <p class="back-web">www.sonvale.ca</p>
  </section>
</body>
</html>
```